KR Stationary Design

Logo, Business Card, Letterhead & Email Signature Design

Target Market(s)

Legal

Colors

Designer to choose colors to be used in the design.

Requirements
Must have
• Gold and Blue are the colours to use. The KR must be inside the Gold Legal Pendulum

```html
<!DOCTYPE html>
<html lang="en">
<head>
<meta charset="utf-8">
<title>KR Stationery – Ravenhill Incorporated</title>
<link href="https://fonts.googleapis.com/css2?family=Roboto+Condensed:wght@400;700&display=swap" rel="stylesheet">
<style>
  :root{
    --gold:#d3ae6c;
    --blue:#3d3d91;
    --orange:#f4854a;
    --ink:#2b2b2b;
    --paper:#fdfdfd;
    --edge:#d9d9d9;
  }
  *{margin:0;padding:0;box-sizing:border-box}
  html,body{width:1200px;height:1200px;overflow:hidden;background:#fff}
  body{position:relative;font-family:"Roboto Condensed",Arial,sans-serif;color:var(--ink)}

  .brand{position:absolute;display:flex;flex-direction:column;align-items:center;color:var(--blue);font-weight:700;line-height:1.05;text-align:center}
  .brand .dot{border-radius:50%;background:var(--gold);margin-bottom:.25em}
  .brand .word{display:block}

  .brand--hero{left:119px;top:230px;width:378px;font-size:58px}
  .brand--hero .dot{width:150px;height:150px;margin-bottom:20px}

  .sheet{position:absolute;background:var(--paper);border:1px solid var(--edge);box-shadow:6px 8px 8px rgba(0,0,0,.18)}

  .letterhead{left:549px;top:25px;width:592px;height:836px}
  .letterhead .brand{left:26px;top:28px;width:104px;font-size:13px}
  .letterhead .brand .dot{width:40px;height:40px}
  .letterhead .reg{position:absolute;left:37px;top:115px;font-size:8.5px}
  .letterhead .rule{position:absolute;left:26px;right:26px;height:1px;background:var(--ink)}
  .letterhead .rule--top{top:128px}
  .letterhead .rule--foot{top:793px}
  .letterhead .footer{position:absolute;left:0;right:0;top:801px;text-align:center;font-size:8.5px}
  .letterhead .contacts{position:absolute;right:26px;top:40px;width:132px;font-size:8.5px;line-height:10.5px}

  .contact-group{display:flex;align-items:flex-start}
  .contact-group .icons{display:flex;flex-direction:column}
  .contact-group .lines{border-left:1px solid var(--gold)}
  .icon{display:block;fill:var(--ink)}

  .card{left:161px;top:664px;width:357px;height:209px}
  .card .brand{left:36px;top:58px;width:112px;font-size:13px}
  .card .brand .dot{width:44px;height:44px}
  .card .name{position:absolute;left:193px;top:58px;color:var(--blue);font-size:14px}
  .card .role{position:absolute;left:193px;top:74px;font-size:12.5px}
  .card .contact-group{position:absolute;left:172px;font-size:12.5px;line-height:14px}

  .signature{left:291px;top:938px;width:858px;height:231px;border:none;box-shadow:6px 6px 6px rgba(0,0,0,.16)}
  .signature .brand{left:20px;top:45px;width:250px;font-size:30px}
  .signature .brand .dot{width:90px;height:90px;margin-bottom:12px}
  .signature .divider{position:absolute;left:283px;top:0;width:3px;height:231px;background:var(--gold)}
  .signature .contact-group{position:absolute;font-size:19.5px;line-height:21px}
</style>
</head>
<body>

  <div class="brand brand--hero" aria-label="Ravenhill Incorporated">
    <span class="dot"></span>
    <span class="word">Ravenhill</span>
    <span class="word">Incorporated</span>
  </div>

  <section class="sheet letterhead">
    <div class="brand"><span class="dot"></span><span class="word">Ravenhill</span><span class="word">Incorporated</span></div>
    <p class="reg">Reg: 2020/555123/07</p>
    <div class="contacts">
      <div class="contact-group">
        <div class="icons" style="width:12px;padding-top:2px">
          <svg class="icon" width="7" height="9" viewBox="0 0 10 14"><path d="M5 0a5 5 0 0 0-5 5c0 4 5 9 5 9s5-5 5-9a5 5 0 0 0-5-5zm0 7a2 2 0 1 1 0-4 2 2 0 0 1 0 4z"/></svg>
        </div>
        <div class="lines" style="padding-left:6px">Block B Oakridge Office Park<br>24 Linden Road<br>North Riverside<br>2040</div>
      </div>
      <div class="contact-group" style="margin-top:7px">
        <div class="icons" style="width:12px;gap:4px;padding-top:2px">
          <svg class="icon" width="7" height="7" viewBox="0 0 10 10"><circle cx="5" cy="5" r="4.4" fill="none" stroke="#2b2b2b"/><path d="M3 2.5c0 2.5 1.5 4.5 4 5l.6-1-1.2-.8-.6.6C5 5.8 4.4 5 4.1 4l.6-.5L4 2.3z"/></svg>
          <svg class="icon" width="7" height="7" viewBox="0 0 10 10"><rect x="1" y="1" width="8" height="2"/><rect x="2" y="4" width="6" height="5"/></svg>
          <svg class="icon" width="7" height="7" viewBox="0 0 10 8"><rect x=".5" y=".5" width="9" height="7" fill="none" stroke="#2b2b2b"/><path d="M.5.5 5 4.5 9.5.5" fill="none" stroke="#2b2b2b"/></svg>
        </div>
        <div class="lines" style="padding-left:6px;line-height:13px">Tel: 011 555 0147<br>Fax: 086 555 0192<br>Email: kim@krravenhill.co.za</div>
      </div>
    </div>
    <div class="rule rule--top"></div>
    <div class="rule rule--foot"></div>
    <p class="footer">Director: Kagiso Robert Ravenhill BA (Northfield), LLB (Eastvale) and HDip Tax Law (WCU)</p>
  </section>

  <section class="sheet card">
    <div class="brand"><span class="dot"></span><span class="word">Ravenhill</span><span class="word">Incorporated</span></div>
    <p class="name">Kim Ravenhill</p>
    <p class="role">Director</p>
    <div class="contact-group" style="top:102px">
      <div class="icons" style="width:15px;gap:5px;padding-top:2px">
        <svg class="icon" width="10" height="10" viewBox="0 0 10 10"><circle cx="5" cy="5" r="4.4" fill="none" stroke="#2b2b2b"/><path d="M3 2.5c0 2.5 1.5 4.5 4 5l.6-1-1.2-.8-.6.6C5 5.8 4.4 5 4.1 4l.6-.5L4 2.3z"/></svg>
        <svg class="icon" width="10" height="10" viewBox="0 0 10 10"><rect x="1" y="1" width="8" height="2"/><rect x="2" y="4" width="6" height="5"/></svg>
        <svg class="icon" width="10" height="8" viewBox="0 0 10 8"><rect x=".5" y=".5" width="9" height="7" fill="none" stroke="#2b2b2b"/><path d="M.5.5 5 4.5 9.5.5" fill="none" stroke="#2b2b2b"/></svg>
      </div>
      <div class="lines" style="padding-left:7px">Tel: 011 555 0147<br>Fax: 086 555 0192<br>Email: kim@krravenhill.co.za</div>
    </div>
    <div class="contact-group" style="top:158px">
      <div class="icons" style="width:15px;padding-top:1px">
        <svg class="icon" width="8" height="11" viewBox="0 0 10 14"><path d="M5 0a5 5 0 0 0-5 5c0 4 5 9 5 9s5-5 5-9a5 5 0 0 0-5-5zm0 7a2 2 0 1 1 0-4 2 2 0 0 1 0 4z"/></svg>
      </div>
      <div class="lines" style="padding-left:7px">Block B, Oakridge Office Park<br>24 Linden Road,<br>North Riverside, 2040.</div>
    </div>
  </section>

  <section class="sheet signature">
    <div class="brand"><span class="dot"></span><span class="word">Ravenhill</span><span class="word">Incorporated</span></div>
    <div class="divider"></div>
    <div class="contact-group" style="left:300px;top:150px">
      <div class="icons" style="width:28px;gap:7px;padding-top:3px">
        <svg class="icon" width="15" height="15" viewBox="0 0 10 10"><circle cx="5" cy="5" r="4.4" fill="none" stroke="#2b2b2b" stroke-width=".7"/><path d="M3 2.5c0 2.5 1.5 4.5 4 5l.6-1-1.2-.8-.6.6C5 5.8 4.4 5 4.1 4l.6-.5L4 2.3z"/></svg>
        <svg class="icon" width="15" height="15" viewBox="0 0 10 10"><rect x="1" y="1" width="8" height="2"/><rect x="2" y="4" width="6" height="5"/></svg>
        <svg class="icon" width="14" height="11" viewBox="0 0 10 8"><rect x=".5" y=".5" width="9" height="7" fill="none" stroke="#2b2b2b" stroke-width=".7"/><path d="M.5.5 5 4.5 9.5.5" fill="none" stroke="#2b2b2b" stroke-width=".7"/></svg>
      </div>
      <div class="lines" style="padding-left:10px">Tel: 011 555 0147<br>Fax: 086 555 0192<br>Email: kim@krravenhill.co.za</div>
    </div>
    <div class="contact-group" style="left:572px;top:152px">
      <div class="icons" style="width:22px;padding-top:2px">
        <svg class="icon" width="11" height="15" viewBox="0 0 10 14"><path d="M5 0a5 5 0 0 0-5 5c0 4 5 9 5 9s5-5 5-9a5 5 0 0 0-5-5zm0 7a2 2 0 1 1 0-4 2 2 0 0 1 0 4z"/></svg>
      </div>
      <div class="lines" style="padding-left:10px">Block B, Oakridge Office Park<br>24 Linden Road,<br>North Riverside, 2040.</div>
    </div>
  </section>

</body>
</html>
```